Elementary School Snapshot of a Wayfinch

Please recreate a poster of our Snapshot of a Wayfinch traits that we desire to have when they graduate from 4th grade. This should be kid-friendly and kid-themed with icons to help communicate the Competencies. See attached six competencies and the "I can" statements next to. Our colors are navy, red and white. Our logo is attached as well. This will be made into a poster and displayed in each classroom, the office, and also used on social media.

```html
<!DOCTYPE html>
<html lang="en">
<head>
<meta charset="utf-8">
<title>Snapshot of a Wayfinch – Early Learners and Elementary School</title>
<link href="https://fonts.googleapis.com/css2?family=Archivo+Black&family=Barlow+Semi+Condensed:wght@800&family=Figtree:wght@500&display=swap" rel="stylesheet">
<style>
  :root {
    --navy: #0b0a3d;
    --red: #a50b0b;
    --white: #ffffff;
    --cream: #fdfbe6;
    --backdrop: #ececec;
  }
  html, body {
    margin: 0;
    width: 978px;
    height: 1200px;
    overflow: hidden;
    background: var(--backdrop);
  }
  .poster {
    position: absolute;
    left: 65px;
    top: 0;
    width: 1180px;
    height: 1669px;
    background: var(--white);
    transform: scale(0.719);
    transform-origin: top left;
    font-family: "Figtree", Arial, sans-serif;
    color: var(--navy);
  }
  .header-band {
    position: absolute;
    left: 0;
    top: 18px;
    width: 1180px;
    height: 141px;
  }
  .district {
    position: absolute;
    left: 44px;
    top: 30px;
    font-size: 17px;
    color: var(--white);
    letter-spacing: 0.2px;
  }
  .title {
    position: absolute;
    left: 42px;
    top: 55px;
    margin: 0;
    font-family: "Archivo Black", Arial, sans-serif;
    font-weight: 400;
    font-size: 41px;
    line-height: 44px;
    color: var(--white);
    text-transform: uppercase;
  }
  .brand-mark {
    position: absolute;
    left: 488px;
    top: 62px;
    display: flex;
    align-items: center;
    gap: 10px;
    font-family: "Archivo Black", Arial, sans-serif;
    font-size: 30px;
    color: var(--red);
  }
  .brand-mark .dot {
    width: 22px;
    height: 22px;
    border-radius: 50%;
    background: var(--navy);
  }
  .school-level {
    position: absolute;
    left: 776px;
    top: 46px;
    margin: 0;
    font-family: "Archivo Black", Arial, sans-serif;
    font-weight: 400;
    font-size: 33px;
    line-height: 42px;
    color: var(--white);
  }
  .tab {
    position: absolute;
    left: 41px;
    top: 188px;
    width: 313px;
    height: 100px;
    background: var(--red);
    border-radius: 24px 24px 0 0;
  }
  .tab span {
    display: block;
    padding: 12px 0 0 22px;
    font-family: "Archivo Black", Arial, sans-serif;
    font-size: 35px;
    color: var(--white);
  }
  .competency-table {
    position: absolute;
    left: 41px;
    top: 258px;
    width: 1098px;
    height: 1367px;
    box-sizing: border-box;
    border: 3px solid var(--navy);
    border-radius: 22px;
    overflow: hidden;
    background: var(--white);
    display: flex;
    flex-direction: column;
  }
  .group {
    display: flex;
    flex: none;
    box-sizing: border-box;
    border-top: 2px solid var(--navy);
  }
  .group:first-child { border-top: none; }
  .trait {
    width: 310px;
    flex: none;
    box-sizing: border-box;
    border-right: 2px solid var(--navy);
    padding: 16px 0 0 24px;
    font-family: "Barlow Semi Condensed", "Arial Narrow", sans-serif;
    font-weight: 800;
    font-size: 36px;
    line-height: 38px;
    color: var(--red);
    text-transform: uppercase;
  }
  .statements {
    flex: 1;
    display: flex;
    flex-direction: column;
  }
  .statement {
    display: flex;
    min-height: 0;
    border-top: 1px solid var(--navy);
    box-sizing: border-box;
  }
  .statement:first-child { border-top: none; }
  .statement.tint { background: var(--cream); }
  .statement p {
    width: 496px;
    flex: none;
    box-sizing: border-box;
    margin: 0;
    border-right: 2px solid var(--navy);
    padding: 0 8px 0 36px;
    display: flex;
    align-items: center;
    font-size: 20px;
    line-height: 25px;
  }
  .statement p span { position: relative; }
  .statement p span::before {
    content: "";
    position: absolute;
    left: -24px;
    top: 8px;
    border-left: 8px solid var(--red);
    border-top: 4.5px solid transparent;
    border-bottom: 4.5px solid transparent;
  }
  .statement .mark-space { flex: 1; }
</style>
</head>
<body>
<main class="poster">
  <svg class="header-band" viewBox="0 0 1180 141" width="1180" height="141" aria-hidden="true">
    <polygon points="0,0 408,0 490,141 0,141" fill="var(--navy)"/>
    <polygon points="408,0 430,0 512,141 490,141" fill="var(--red)"/>
    <polygon points="742,0 757,0 690,141 672,141" fill="var(--navy)"/>
    <polygon points="757,0 1180,0 1180,141 690,141" fill="var(--red)"/>
  </svg>
  <div class="district">HARROW CREEK PUBLIC SCHOOLS</div>
  <h1 class="title">Snapshot<br>of a Wayfinch</h1>
  <div class="brand-mark"><span class="dot"></span>Wayfinch</div>
  <h2 class="school-level">Early Learners and<br>Elementary School</h2>

  <div class="tab"><span>COMPETENCY</span></div>

  <section class="competency-table">
    <div class="group" style="height:251px">
      <div class="trait">Communicator</div>
      <div class="statements">
        <div class="statement tint" style="flex:89 1 0"><p><span>I can use words, writing, and<br>pictures to clearly share ideas.</span></p><div class="mark-space"></div></div>
        <div class="statement" style="flex:91 1 0"><p><span>I can look at the speaker and listen<br>carefully to understand what they<br>are saying.</span></p><div class="mark-space"></div></div>
        <div class="statement tint" style="flex:72 1 0"><p><span>I know how to adjust my communication<br>for different places and people.</span></p><div class="mark-space"></div></div>
      </div>
    </div>
    <div class="group" style="height:234px">
      <div class="trait">Critical<br>Thinker</div>
      <div class="statements">
        <div class="statement" style="flex:81 1 0"><p><span>I can ask questions like "why" and "how"<br>to learn more about the world.</span></p><div class="mark-space"></div></div>
        <div class="statement tint" style="flex:77 1 0"><p><span>When faced with a problem, I can be creative<br>and come up with different solutions.</span></p><div class="mark-space"></div></div>
        <div class="statement" style="flex:74 1 0"><p><span>I can use facts and clues to help make<br>wise decisions.</span></p><div class="mark-space"></div></div>
      </div>
    </div>
    <div class="group" style="height:224px">
      <div class="trait">Responsible</div>
      <div class="statements">
        <div class="statement tint" style="flex:79 1 0"><p><span>I can take ownership of my actions and<br>remember to complete my job.</span></p><div class="mark-space"></div></div>
        <div class="statement" style="flex:69 1 0"><p><span>I can take care of my belongings and<br>always try my best in schoolwork.</span></p><div class="mark-space"></div></div>
        <div class="statement tint" style="flex:73 1 0"><p><span>I can tell the truth and act with integrity<br>even when no one is watching.</span></p><div class="mark-space"></div></div>
      </div>
    </div>
    <div class="group" style="height:220px">
      <div class="trait">Adaptable</div>
      <div class="statements">
        <div class="statement" style="flex:78 1 0"><p><span>When a plan changes or a task is hard,<br>I can stay calm and try a new way.</span></p><div class="mark-space"></div></div>
        <div class="statement tint" style="flex:67 1 0"><p><span>I can learn from mistakes and use past<br>knowledge to try new things.</span></p><div class="mark-space"></div></div>
        <div class="statement" style="flex:73 1 0"><p><span>I can work and play well with people<br>who are different from me.</span></p><div class="mark-space"></div></div>
      </div>
    </div>
    <div class="group" style="height:211px">
      <div class="trait">Collaborator</div>
      <div class="statements">
        <div class="statement tint" style="flex:70 1 0"><p><span>I can share ideas and work together<br>with a group to reach a common goal.</span></p><div class="mark-space"></div></div>
        <div class="statement" style="flex:73 1 0"><p><span>I can listen to my teammates and<br>respect their different ideas.</span></p><div class="mark-space"></div></div>
        <div class="statement tint" style="flex:67 1 0"><p><span>I can know when to share, when to<br>help others, and when to be the leader.</span></p><div class="mark-space"></div></div>
      </div>
    </div>
    <div class="group" style="height:221px">
      <div class="trait">Compassionate</div>
      <div class="statements">
        <div class="statement" style="flex:72 1 0"><p><span>I can be empathetic, noticing how others<br>are feeling (happy, sad, frustrated).</span></p><div class="mark-space"></div></div>
        <div class="statement tint" style="flex:67 1 0"><p><span>I can use kind words and gentle actions<br>to support their friends.</span></p><div class="mark-space"></div></div>
        <div class="statement" style="flex:80 1 0"><p><span>I can look for ways to help their school<br>and the community.</span></p><div class="mark-space"></div></div>
      </div>
    </div>
  </section>
</main>
</body>
</html>
```